Business Card - Apex Wellness

Please use the logo / design elements and font to design a business card that is eye catching and informative. If using "Direct Primary Care" logo element, you don't have to spell it out in the text.

Dr. Brendan Halvik
Apex Wellness - Direct Primary Care
4817 Tillbrook Rd. Suite 305
Harlow Springs, AR 72950
Phone: 479-555-0137
ApexWellnessAR.example

```html
<!DOCTYPE html>
<html lang="en">
<head>
<meta charset="utf-8">
<title>Apex Wellness – Business Card</title>
<link rel="stylesheet" href="https://fonts.googleapis.com/css2?family=Montserrat:wght@400;500&family=Poppins:wght@500&display=swap">
<style>
  :root {
    --page: #dedede;
    --navy: #08142f;
    --paper: #f1f6fc;
    --ink: #0b1735;
    --muted: #5a5d63;
    --accent: #2f5fb3;
    --sky: #1aa8e0;
    --white: #ffffff;
  }
  * { margin: 0; padding: 0; box-sizing: border-box; }
  html, body { width: 1200px; height: 1200px; overflow: hidden; }
  body { background: var(--page); position: relative; font-family: "Montserrat", sans-serif; }

  .card { position: absolute; left: 179px; width: 861px; height: 496px; }
  .card--front { top: 84px; background: var(--navy); }
  .card--back { top: 622px; background: var(--paper); }

  .front-mark {
    position: absolute; left: 50%; top: 180px; width: 34px; height: 34px;
    margin-left: -17px; border-radius: 50%; background: var(--sky);
  }
  .front-name {
    position: absolute; left: 0; right: 0; top: 262px; text-align: center;
    font-family: "Poppins", sans-serif; font-weight: 500; font-size: 56px;
    letter-spacing: -1px; color: var(--white); line-height: 1;
  }

  .back-name {
    position: absolute; left: 48px; top: 88px;
    font-family: "Poppins", sans-serif; font-weight: 500; font-size: 42px;
    letter-spacing: -1px; color: var(--ink); line-height: 1;
  }

  .person { position: absolute; left: 461px; top: 86px; }
  .person-name { font-weight: 500; font-size: 31px; color: var(--ink); line-height: 1.1; }
  .person-title { font-weight: 400; font-size: 23px; color: var(--muted); line-height: 1.3; }
  .person-rule { width: 56px; height: 3px; background: var(--accent); margin-top: 10px; }

  .address {
    position: absolute; left: 45px; top: 340px; font-style: normal;
    font-size: 22.5px; color: var(--muted); line-height: 37px; font-weight: 400;
  }

  .contacts { position: absolute; left: 461px; top: 318px; list-style: none; }
  .contacts li {
    display: flex; align-items: center; height: 31px;
    font-size: 22px; color: var(--muted); font-weight: 400;
  }
  .contacts svg { width: 20px; height: 20px; margin-right: 11px; flex: none; }
</style>
</head>
<body>
  <section class="card card--front">
    <span class="front-mark"></span>
    <p class="front-name">Apex Wellness</p>
  </section>

  <section class="card card--back">
    <p class="back-name">Apex Wellness</p>

    <div class="person">
      <p class="person-name">Dr. Brendan Halvik</p>
      <p class="person-title">Founder</p>
      <div class="person-rule"></div>
    </div>

    <address class="address">
      4817 Tillbrook Rd. Suite 305<br>
      Harlow Springs, AR 72950
    </address>

    <ul class="contacts">
      <li>
        <svg viewBox="0 0 24 24" aria-hidden="true"><path fill="var(--accent)" d="M6.6 10.8a15.1 15.1 0 0 0 6.6 6.6l2.2-2.2c.3-.3.7-.4 1-.2 1.1.4 2.3.6 3.6.6.6 0 1 .4 1 1V20c0 .6-.4 1-1 1A17 17 0 0 1 3 4c0-.6.4-1 1-1h3.5c.6 0 1 .4 1 1 0 1.3.2 2.5.6 3.6.1.3 0 .7-.2 1z"/><path fill="none" stroke="var(--accent)" stroke-width="1.8" d="M14 3a7 7 0 0 1 7 7M14 6.5a3.5 3.5 0 0 1 3.5 3.5"/></svg>
        479-555-0137
      </li>
      <li>
        <svg viewBox="0 0 24 24" aria-hidden="true"><rect x="2" y="5" width="20" height="14" fill="var(--accent)"/><path d="M2 5l10 8 10-8M2 19l7.5-7M22 19l-7.5-7" fill="none" stroke="var(--paper)" stroke-width="1.4"/></svg>
        info@apexwellnessar.example
      </li>
      <li>
        <svg viewBox="0 0 24 24" aria-hidden="true"><g fill="none" stroke="var(--accent)" stroke-width="1.6"><circle cx="12" cy="12" r="10"/><ellipse cx="12" cy="12" rx="4.5" ry="10"/><path d="M2 12h20M4 7h16M4 17h16M12 2v20"/></g></svg>
        www.ApexWellnessAR.example
      </li>
    </ul>
  </section>
</body>
</html>
```